Executive Business Consulting for Telco Companies and Telco Start up companies

1.) Looking for an appealing and action oriented business card design.
2.)The target companies to work with start-ups and existing companies that focus on Business to Business applications
3.) For "OKRA", a Belgium based Executive consultancy company specialised in global reach starting from the centre of Europe = Brussels.
4.) Our core competence is the Go To Market in All major global regions, incl North America, Latin America, Asia, Japan, Europe and Africa.
5.) Design should be appealing to CEO, CFO and Venture Funds signalling; Expertise, Stability, Maturity and Commitment
6.) Preferred color scheme is Blue focussed and using a modern FONT.
7.) Logo design is included (uploaded)

Target Market(s)

Telecommunication Market. Companies in a B2B business model, developping services or applications to make business run more profitable

Industry/Entity Type

Business

Contact Information for Business Card

Company Name: OKRA
Name: Joris Vandelay
Titel: Managing Director
Address: Kalkweg 58 , B-9170 Meerdonk , Belgium
Tel: + 32 471 208 364
Email: joris_vandelay@plimbox.example
LinkedIn: be.netprofilo.example/in/jorisvandelay/

Font styles to use
Serif

Colors
0455a3
3277b5

Requirements
Must have
• Second Side Text: Driving Global Market Entry and Growth

```html
<!DOCTYPE html>
<html lang="en">
<head>
<meta charset="utf-8">
<title>OKRA – Business Card</title>
<link href="https://fonts.googleapis.com/css2?family=Exo+2:wght@400;500;600;700&display=swap" rel="stylesheet">
<style>
  :root {
    --page: #e8e8e8;
    --card-top: #2e3033;
    --card-bottom: #1b1c1e;
    --blue: #0455a3;
    --blue-bright: #2a86c8;
    --blue-soft: #3277b5;
    --silver: #cfd3d8;
    --text: #e4e6e8;
    --faint: rgba(255, 255, 255, 0.05);
  }
  * { margin: 0; padding: 0; box-sizing: border-box; }
  html, body {
    width: 1200px; height: 720px; overflow: hidden;
    background: var(--page);
    font-family: "Exo 2", sans-serif;
  }
  .stage { position: relative; width: 1200px; height: 720px; }
  .card {
    position: absolute; top: 202px;
    width: 540px; height: 316px;
    border-radius: 20px; overflow: hidden;
    background: linear-gradient(160deg, var(--card-top), var(--card-bottom));
    color: var(--text);
  }
  .card--front { left: 40px; }
  .card--back { left: 620px; }

  /* front */
  .brand-mark {
    position: absolute; left: 0; right: 0; top: 100px;
    display: flex; justify-content: center; align-items: center; gap: 18px;
  }
  .brand-mark__dot {
    width: 54px; height: 54px; border-radius: 50%;
    background: var(--blue-soft);
  }
  .brand-mark__name {
    font-size: 68px; font-weight: 700; letter-spacing: 3px;
    color: var(--silver); line-height: 1;
  }
  .tagline {
    position: absolute; left: 0; right: 0; top: 273px;
    text-align: center; font-size: 14px; font-weight: 600;
    color: var(--blue-bright); text-transform: uppercase;
  }

  /* back */
  .backdrop-circle {
    position: absolute; left: 295px; top: 5px;
    width: 310px; height: 310px; border-radius: 50%;
    background: var(--faint);
    border: 3px solid rgba(255,255,255,0.07);
  }
  .brand-name {
    position: absolute; left: 34px; top: 52px;
    font-size: 44px; font-weight: 700; letter-spacing: 2px;
    color: var(--silver); line-height: 1;
  }
  .person { position: absolute; left: 34px; top: 160px; }
  .person__name {
    font-size: 19px; font-weight: 700; color: var(--blue-bright);
    text-transform: uppercase; line-height: 1.1;
  }
  .person__role { font-size: 14px; font-weight: 600; color: #f2f2f2; margin-top: 2px; }
  .divider {
    position: absolute; left: 25px; right: 27px; top: 219px;
    height: 1px; background: var(--blue-bright);
  }
  .contact {
    position: absolute; display: flex; align-items: center; gap: 6px;
    font-size: 14.5px; color: var(--text); white-space: nowrap;
  }
  .contact svg { width: 14px; height: 14px; flex: none; }
  .contact--address { left: 32px; top: 229px; }
  .contact--phone { left: 32px; top: 252px; }
  .contact--email { left: 212px; top: 252px; }
  .contact--profile { left: 32px; top: 275px; }
  .icon-square { width: 11px; height: 11px; background: var(--blue-soft); margin: 0 1.5px; flex: none; }
</style>
</head>
<body>
<main class="stage">

  <section class="card card--front" aria-label="Card front">
    <div class="brand-mark">
      <span class="brand-mark__dot"></span>
      <span class="brand-mark__name">OKRA</span>
    </div>
    <p class="tagline">Driving Global Market Entry and Growth</p>
  </section>

  <section class="card card--back" aria-label="Card back">
    <div class="backdrop-circle"></div>
    <div class="brand-name">OKRA</div>

    <div class="person">
      <h1 class="person__name">Joris Vandelay</h1>
      <p class="person__role">Managing Director</p>
    </div>

    <div class="divider"></div>

    <p class="contact contact--address">
      <svg viewBox="0 0 14 14" aria-hidden="true"><path d="M7 1a3.5 3.5 0 0 0-3.5 3.5C3.5 7.2 7 11 7 11s3.5-3.8 3.5-6.5A3.5 3.5 0 0 0 7 1zm0 4.8a1.3 1.3 0 1 1 0-2.6 1.3 1.3 0 0 1 0 2.6z" fill="#3277b5"/><path d="M2 12.5h10" stroke="#3277b5" stroke-width="1.2"/></svg>
      Kalkweg 58, B-9170 Meerdonk, Belgium
    </p>
    <p class="contact contact--phone">
      <svg viewBox="0 0 14 14" aria-hidden="true"><path d="M3.2 1.5l2 2.4-1.1 1.4c.7 1.6 2 2.9 3.6 3.6l1.4-1.1 2.4 2-1.2 2C6.4 11.6 2.4 7.6 1.2 2.7z" fill="#3277b5"/></svg>
      +32 471 208 364
    </p>
    <p class="contact contact--email">
      <svg viewBox="0 0 14 14" aria-hidden="true"><rect x="1" y="3" width="12" height="8.5" fill="#3277b5"/><path d="M1 3.3l6 4.4 6-4.4" stroke="#1b1c1e" stroke-width="1" fill="none"/></svg>
      joris_vandelay@plimbox.example
    </p>
    <p class="contact contact--profile">
      <span class="icon-square"></span>
      netprofilo.example/in/jorisvandelay
    </p>
  </section>

</main>
</body>
</html>
```